Cover Page for Financial Statements

We need a cover page designed for our Financial Statements. It will need to include our business logo and the Chartered accountant logo.
We have included our current title page ( image titled full.png ) to show all the information that is needed to be included such as the title 'Financial Statements' and 'The year ended March 2023'. We would like to see designs that reflect our logo but also adds some interest with objects / deisngs that fill up more of the page.

Industry/Entity Type

Accounting

Font styles to use
Serif
Sans Serif

Colors

Designer to choose only greyscale colors for use in the design.

Requirements
Must have
• - A4 document size, our logo, Chartered Accountant Logo
Should not have
• Bright Colors

```html
<!DOCTYPE html>
<html lang="en">
<head>
<meta charset="UTF-8">
<title>Financial Statements Cover</title>
<link href="https://fonts.googleapis.com/css2?family=Montserrat:wght@500;600;700;800&display=swap" rel="stylesheet">
<style>
  :root {
    --backdrop: #c9c9ca;
    --paper: #f4f4f4;
    --mist: #d9d9d9;
    --mist-deep: #b4b4b4;
    --mist-pale: #ebebeb;
    --charcoal: #2a2a2a;
    --charcoal-soft: rgba(42, 42, 42, 0.72);
    --slate: #707070;
    --ink: #1d1d1f;
  }
  * { margin: 0; padding: 0; box-sizing: border-box; }
  html, body {
    width: 1200px;
    height: 904px;
    overflow: hidden;
    background: var(--backdrop);
    font-family: "Montserrat", Arial, sans-serif;
  }
  .cover {
    position: absolute;
    left: 310px;
    top: 42px;
    width: 580px;
    height: 820px;
    background: var(--paper);
    overflow: hidden;
    box-shadow: 0 10px 30px rgba(0,0,0,0.18);
  }
  .cover__art {
    position: absolute;
    inset: 0;
  }
  .cover__photo {
    position: absolute;
    left: 0;
    top: 440px;
    width: 580px;
    height: 380px;
    background: linear-gradient(160deg, var(--mist-pale) 0%, var(--mist) 45%, var(--mist-deep) 75%, #cfcfcf 100%);
  }
  .cover__content {
    position: absolute;
    left: 48px;
    top: 96px;
    width: 330px;
  }
  .logo-row {
    display: flex;
    justify-content: space-between;
    align-items: center;
    margin-bottom: 34px;
  }
  .logo {
    display: flex;
    align-items: center;
    gap: 7px;
    font-weight: 600;
    color: var(--ink);
    white-space: nowrap;
  }
  .logo--institute { font-size: 9px; letter-spacing: 0.06em; text-transform: uppercase; }
  .logo--institute .logo__mark {
    width: 16px; height: 16px; border-radius: 50%; background: var(--slate);
  }
  .logo--firm { font-size: 13px; letter-spacing: 0.08em; text-transform: uppercase; }
  .logo--firm .logo__mark {
    width: 14px; height: 14px; background: var(--charcoal);
  }
  .company-name {
    font-size: 20px;
    font-weight: 700;
    line-height: 1.2;
    color: var(--ink);
    margin-bottom: 22px;
  }
  .title {
    font-size: 46px;
    font-weight: 800;
    line-height: 1.0;
    color: var(--ink);
    margin-bottom: 10px;
  }
  .period {
    font-size: 14px;
    font-weight: 700;
    color: var(--ink);
  }
</style>
</head>
<body>
  <main class="cover">
    <div class="cover__photo" role="img" aria-label="Soft grey photograph of a hand holding a pen over a financial spreadsheet"></div>
    <svg class="cover__art" width="580" height="820" viewBox="0 0 580 820" aria-hidden="true">
      <rect class="band-top" x="0" y="0" width="580" height="60" fill="var(--mist)"/>
      <polygon class="stripe-dark" points="395,60 580,60 580,150 500,150 470,440 385,440" fill="var(--charcoal)"/>
      <polygon class="stripe-dark-fade" points="385,440 470,440 430,740" fill="var(--charcoal-soft)"/>
      <polygon class="stripe-slate" points="500,150 580,150 580,440 470,440" fill="var(--slate)"/>
      <polygon class="facet-pale" points="0,560 0,820 300,820" fill="rgba(255,255,255,0.35)"/>
    </svg>
    <section class="cover__content">
      <div class="logo-row">
        <div class="logo logo--institute"><span class="logo__mark"></span>Certified Ledger Institute</div>
        <div class="logo logo--firm"><span class="logo__mark"></span>Meridian Ledger</div>
      </div>
      <p class="company-name">Meridian Ledger Accounting<br>&amp; Advisory Limited</p>
      <h1 class="title">Financial<br>Statements</h1>
      <p class="period">For the Year Ended 31 March, 2023</p>
    </section>
  </main>
</body>
</html>
```